Summit Grading a Builders LLC business card

My current business card is very plain. it has my logo and contact information. I woud like something that stands out from the rest. please take a look at my website to see about my company.

Compayt Name - Summit Grading And Builders
Owner - Martin Kowalczyk
Business Address
Business Website - www.summitgradingandbuilders.example
Email - Summitgradingandbuilders@mailbox.example
Phone - 555-214-7390
Fax - 555-806-3127

Target Market(s)

Everyone age tang is 18 - 85

Industry/Entity Type

Business

Contact Information for Business Card

Nice and professional all in one.

Font styles to use
Serif
Other font styles liked:
• Up to you

Requirements
Must have
• All contact info. The design is up to you.
Nice to have
• All the contact info the design is up to you
Should not have
• I don't have any

```html
<!DOCTYPE html>
<html lang="en">
<head>
<meta charset="utf-8">
<title>Summit Grading &amp; Builders LLC – Business Card</title>
<link href="https://fonts.googleapis.com/css2?family=Roboto+Slab:wght@800&family=Mulish:wght@700;800&display=swap" rel="stylesheet">
<style>
  :root {
    --page: #e9e6e1;
    --asphalt-dark: #2f2f2f;
    --asphalt-mid: #474747;
    --asphalt-light: #6f6f6f;
    --band: #2a2a2a;
    --dash: #d4d4d4;
    --white: #ffffff;
    --orange: #f28c1e;
    --badge-fill: #8a8a8a;
    --badge-edge: #b5b5b5;
  }
  * { margin: 0; padding: 0; box-sizing: border-box; }
  html, body { width: 1095px; height: 1200px; overflow: hidden; }
  body {
    background: var(--page);
    font-family: "Mulish", Arial, sans-serif;
    position: relative;
  }
  .card {
    position: absolute;
    left: 157px;
    width: 780px;
    height: 464px;
    overflow: hidden;
    box-shadow: 0 3px 10px rgba(0,0,0,.25);
  }
  .card--front { top: 110px; }
  .card--back { top: 640px; }

  .asphalt { position: absolute; inset: 0; }
  .card--front .asphalt {
    background: radial-gradient(ellipse at 50% 40%, var(--asphalt-mid), var(--asphalt-dark) 80%);
  }
  .card--back .asphalt {
    background: radial-gradient(ellipse at 50% 60%, #7a7a7a, var(--asphalt-light) 85%);
  }

  .lane-dashes {
    position: absolute; left: 0; right: 0; height: 9px;
    background: repeating-linear-gradient(90deg, var(--dash) 0 22px, transparent 22px 30px);
  }

  /* Front */
  .front-title {
    position: absolute; top: 72px; left: 0; right: 0;
    text-align: center;
    font-family: "Roboto Slab", Georgia, serif;
    font-weight: 800;
    color: var(--white);
    font-size: 48px; line-height: 60px;
  }
  .front-title .llc { font-size: 32px; }
  .badges {
    position: absolute; top: 236px; left: 0; right: 0;
    display: flex; justify-content: center; gap: 50px;
  }
  .badge { width: 74px; height: 74px; }
  .card--front .lane-dashes { top: 353px; }
  .web-band {
    position: absolute; left: 0; right: 0; top: 366px; bottom: 0;
    background: var(--band);
    display: flex; align-items: center; justify-content: center;
  }
  .website { color: var(--white); font-weight: 800; font-size: 25px; }

  /* Back */
  .title-band {
    position: absolute; left: 0; right: 0; top: 0; height: 98px;
    background: var(--band);
    display: flex; align-items: center; justify-content: center;
  }
  .back-title {
    font-family: "Roboto Slab", Georgia, serif;
    font-weight: 800;
    color: var(--white); font-size: 30px;
  }
  .back-title .llc { font-size: 20px; }
  .card--back .lane-dashes { top: 98px; }

  .owner {
    position: absolute; left: 88px; top: 160px;
    display: flex; align-items: center; gap: 18px;
  }
  .owner-name { color: var(--white); font-weight: 800; font-size: 25px; line-height: 30px; }
  .owner-role { color: var(--orange); font-weight: 800; font-size: 21px; line-height: 26px; }

  .contact-list { position: absolute; left: 95px; top: 244px; list-style: none; }
  .contact-item {
    display: flex; align-items: center; gap: 22px;
    height: 38px; margin-bottom: 3px;
    color: var(--white); font-weight: 800; font-size: 21px;
  }
  .contact-item:last-child { margin-top: 6px; }
  .icon { width: 30px; height: 30px; flex: none; }
</style>
</head>
<body>

<section class="card card--front" aria-label="Card front">
  <div class="asphalt" role="img" aria-label="Dark asphalt surface texture"></div>
  <h1 class="front-title">SUMMIT GRADING<br>&amp; BUILDERS <span class="llc">LLC</span></h1>
  <div class="badges">
    <svg class="badge" viewBox="0 0 74 74" role="img" aria-label="Partner badge"><circle cx="37" cy="37" r="34" fill="var(--badge-fill)" stroke="var(--badge-edge)" stroke-width="3"/></svg>
    <svg class="badge" viewBox="0 0 74 74" role="img" aria-label="Partner badge"><circle cx="37" cy="37" r="34" fill="var(--badge-fill)" stroke="var(--badge-edge)" stroke-width="3"/></svg>
    <svg class="badge" viewBox="0 0 74 74" role="img" aria-label="Partner badge"><circle cx="37" cy="37" r="34" fill="var(--badge-fill)" stroke="var(--badge-edge)" stroke-width="3"/></svg>
  </div>
  <div class="lane-dashes"></div>
  <div class="web-band">
    <p class="website">www.summitgradingandbuilders.example</p>
  </div>
</section>

<section class="card card--back" aria-label="Card back">
  <div class="asphalt" role="img" aria-label="Grey asphalt surface texture"></div>
  <div class="title-band">
    <h2 class="back-title">SUMMIT GRADING &amp; BUILDERS <span class="llc">LLC</span></h2>
  </div>
  <div class="lane-dashes"></div>

  <div class="owner">
    <svg class="icon" style="width:42px;height:42px" viewBox="0 0 42 42" aria-hidden="true">
      <circle cx="21" cy="21" r="19" fill="none" stroke="var(--orange)" stroke-width="2.5"/>
      <circle cx="21" cy="16" r="6.5" fill="var(--orange)"/>
      <path d="M9 33 C11 25 31 25 33 33 Z" fill="var(--orange)"/>
    </svg>
    <div>
      <p class="owner-name">MARTIN KOWALCZYK</p>
      <p class="owner-role">Owner</p>
    </div>
  </div>

  <ul class="contact-list">
    <li class="contact-item">
      <svg class="icon" viewBox="0 0 30 30" aria-hidden="true">
        <circle cx="15" cy="15" r="13" fill="none" stroke="var(--orange)" stroke-width="2"/>
        <path d="M10 8 L13 8 L14 12 L12 13.5 C13 16 14 17 16.5 18 L18 16 L22 17 L22 20 C15 21 9 15 10 8 Z" fill="var(--orange)"/>
      </svg>
      <span>555-214-7390</span>
    </li>
    <li class="contact-item">
      <svg class="icon" viewBox="0 0 30 30" aria-hidden="true">
        <circle cx="15" cy="15" r="13" fill="none" stroke="var(--orange)" stroke-width="2"/>
        <rect x="11" y="7.5" width="8" height="5" fill="var(--orange)"/>
        <rect x="8" y="12" width="14" height="7" rx="1" fill="var(--orange)"/>
        <rect x="11" y="17" width="8" height="5" fill="none" stroke="var(--orange)" stroke-width="1.5"/>
      </svg>
      <span>555-806-3127</span>
    </li>
    <li class="contact-item">
      <svg class="icon" viewBox="0 0 30 30" aria-hidden="true">
        <circle cx="15" cy="15" r="13" fill="none" stroke="var(--orange)" stroke-width="2"/>
        <rect x="8" y="10" width="14" height="10" fill="none" stroke="var(--orange)" stroke-width="1.8"/>
        <path d="M8 10 L15 16 L22 10" fill="none" stroke="var(--orange)" stroke-width="1.8"/>
      </svg>
      <span>Summitgradingandbuilders@mailbox.example</span>
    </li>
    <li class="contact-item">
      <svg class="icon" viewBox="0 0 30 30" aria-hidden="true">
        <circle cx="15" cy="15" r="13" fill="none" stroke="var(--orange)" stroke-width="2"/>
        <path d="M15 23 C11 18 10 15.5 10 13 A5 5 0 0 1 20 13 C20 15.5 19 18 15 23 Z" fill="var(--orange)"/>
        <circle cx="15" cy="13" r="2" fill="var(--asphalt-light)"/>
      </svg>
      <span>48 Harbor Rd, Eastfield, NY 10990</span>
    </li>
  </ul>
</section>

</body>
</html>
```